Corvane Holdings , new business card design

investment firm with corporate clients . need double sided business card , vertical and horizontal options ,logo must be clear. prefer pantone colors only and sharp design. website also www.corvane-example.ae

Khalid Bin Rashed
Managing Director
Tel. +971 4 000 3829
Mobile +971 50 000 4172
khalid@corvane-example.ae
Palm Crest Tower, officw 18-B07, Qasr Gardens, Dubai

Contact Information for Business Card

Khalid Bin Rashed
Managing Director

Font styles to use
Serif

Colors

Designer to choose colors to be used in the design.

```html
<!DOCTYPE html>
<html lang="en">
<head>
<meta charset="utf-8">
<title>Corvane Holdings – Business Card</title>
<link rel="stylesheet" href="https://fonts.googleapis.com/css2?family=Open+Sans:wght@300;400;600;700&display=swap">
<style>
  :root {
    --navy: #00235a;
    --card-grey: #c6c5c4;
    --paper: #ffffff;
    --ink: #1a1a1a;
  }
  * { margin: 0; padding: 0; box-sizing: border-box; }
  html, body {
    width: 1200px; height: 1200px; overflow: hidden;
    background: var(--paper);
    font-family: "Open Sans", Arial, sans-serif;
  }
  .canvas { position: relative; width: 1200px; height: 1200px; }

  .card {
    position: absolute;
    width: 541px; height: 900px;
    background: var(--navy);
  }
  .card-front { left: 41px; top: 72px; }
  .card-back { left: 624px; top: 256px; }

  .card-face {
    position: absolute;
    left: 30px; top: 30px;
    width: 481px; height: 840px;
    border-radius: 36px;
  }
  .card-front .card-face { background: var(--paper); }
  .card-back .card-face { background: var(--card-grey); }

  .brand {
    position: absolute;
    left: 0; right: 0; top: 382px;
    text-align: center;
    color: var(--navy);
    font-weight: 300;
    text-transform: uppercase;
  }
  .brand-line { display: block; }
  .brand-main { font-size: 52px; letter-spacing: 22px; padding-left: 22px; line-height: 64px; }
  .brand-sub { font-size: 20px; letter-spacing: 21px; padding-left: 21px; line-height: 32px; margin-top: 6px; }

  .person {
    position: absolute;
    left: 0; right: 0; top: 144px;
    text-align: center;
    color: var(--navy);
  }
  .person-name { font-size: 32px; font-weight: 700; line-height: 40px; }
  .person-title { font-size: 28px; font-weight: 400; line-height: 36px; margin-top: 8px; }

  .contacts { position: absolute; left: 0; top: 0; width: 100%; height: 100%; }
  .contact { position: absolute; left: 82px; width: 356px; }
  .contact-bar {
    position: absolute; left: 0; top: 0;
    width: 356px; height: 100%;
    background: var(--navy);
    color: var(--paper);
    font-weight: 300;
    font-size: 22px;
    line-height: 28px;
    padding-left: 21px;
    display: flex; flex-direction: column; justify-content: center;
    overflow: hidden;
  }
  .contact-bar::before {
    content: "";
    position: absolute;
    left: -46px; top: 50%;
    width: 48px; height: 48px;
    margin-top: -24px;
    border-radius: 50%;
    background: var(--card-grey);
  }
  .contact-icon {
    position: absolute;
    left: -42px; top: 50%;
    width: 34px; height: 34px;
    margin-top: -17px;
  }
  .contact-phone { top: 552px; height: 33px; }
  .contact-email { top: 596px; height: 34px; }
  .contact-mobile { top: 642px; height: 34px; }
  .contact-address { top: 686px; height: 66px; }
</style>
</head>
<body>
<div class="canvas">

  <section class="card card-front" aria-label="Card front">
    <div class="card-face">
      <div class="brand">
        <span class="brand-line brand-main">Corvane</span>
        <span class="brand-line brand-sub">Holdings</span>
      </div>
    </div>
  </section>

  <section class="card card-back" aria-label="Card back">
    <div class="card-face">
      <div class="person">
        <p class="person-name">Khalid Bin Rashed</p>
        <p class="person-title">Managing Director</p>
      </div>

      <div class="contacts">
        <div class="contact contact-phone">
          <div class="contact-bar">+971 4 000 3829</div>
          <svg class="contact-icon" viewBox="0 0 34 34" aria-hidden="true">
            <circle cx="17" cy="17" r="15.5" fill="none" stroke="var(--navy)" stroke-width="2"/>
            <path d="M11 9.5l3 -0.5 2 4.5 -2 1.5c1 2.5 2.5 4 5 5l1.5 -2 4.5 2 -0.5 3c-7 1 -14.5 -6.5 -13.5 -13.5z" fill="none" stroke="var(--navy)" stroke-width="1.8" stroke-linejoin="round"/>
          </svg>
        </div>

        <div class="contact contact-email">
          <div class="contact-bar">khalid@corvane-example.ae</div>
          <svg class="contact-icon" viewBox="0 0 34 34" aria-hidden="true">
            <circle cx="17" cy="17" r="15.5" fill="none" stroke="var(--navy)" stroke-width="2"/>
            <path d="M8 16l17 -7 -6 17 -3 -7z" fill="var(--navy)"/>
            <path d="M16 19l9 -10" stroke="var(--card-grey)" stroke-width="1.5"/>
          </svg>
        </div>

        <div class="contact contact-mobile">
          <div class="contact-bar">+971 50 000 4172</div>
          <svg class="contact-icon" viewBox="0 0 34 34" aria-hidden="true">
            <circle cx="17" cy="17" r="15.5" fill="none" stroke="var(--navy)" stroke-width="2"/>
            <rect x="12" y="8" width="10" height="18" rx="2" fill="none" stroke="var(--navy)" stroke-width="1.8"/>
            <circle cx="17" cy="23" r="1.2" fill="var(--navy)"/>
          </svg>
        </div>

        <div class="contact contact-address">
          <div class="contact-bar">
            <span>Palm Crest Tower, officw 18-B07,</span>
            <span>Qasr Gardens, Dubai</span>
          </div>
          <svg class="contact-icon" viewBox="0 0 34 34" aria-hidden="true">
            <circle cx="17" cy="17" r="15.5" fill="none" stroke="var(--navy)" stroke-width="2"/>
            <path d="M17 27c-4 -5 -7 -8.5 -7 -12a7 7 0 0 1 14 0c0 3.5 -3 7 -7 12z" fill="none" stroke="var(--navy)" stroke-width="2" stroke-linejoin="round"/>
            <circle cx="17" cy="15" r="2.6" fill="var(--navy)"/>
          </svg>
        </div>
      </div>
    </div>
  </section>

</div>
</body>
</html>
```